Webdesign mit Grundfarbe Weinrot für allgemeine Steuerberatung
Zielgruppe
Allgemeine Steuerberatung. Zielgruppe ist breit gefächert, allerdings soll die Webseite eher den Jungunternehmer ansprechen.
Aufgabenstellung
Die Grundfarbe sollte weinrot sein.

```html
<!DOCTYPE html>
<html lang="de">
<head>
<meta charset="utf-8">
<title>Steuerberatung Lindner – Gießen</title>
<link href="https://fonts.googleapis.com/css2?family=Tinos:wght@400;700&family=Open+Sans:wght@400;600;700&display=swap" rel="stylesheet">
<style>
:root{
  --wine:#4d1024;
  --red:#d24f59;
  --grey:#efefef;
  --card:#f3f3f3;
  --ink:#1f1f1f;
  --text:#4a4a4a;
  --footer:#2b2527;
  --white:#fff;
}
*{box-sizing:border-box;margin:0;padding:0}
html,body{width:1200px;height:2701px;overflow:hidden;background:var(--white)}
body{position:relative;font-family:"Open Sans",sans-serif;color:var(--text)}
.abs{position:absolute}
.serif{font-family:"Tinos",serif;color:var(--ink);font-weight:400}
.hero-bg{left:0;top:0;width:985px;height:629px;background:var(--grey)}
.brand{left:0;top:0;width:301px;height:111px;background:var(--red);border-bottom-right-radius:3px;display:flex;align-items:center;justify-content:center;gap:10px;padding-left:60px}
.brand-name{font-family:"Tinos",serif;color:var(--white);font-size:21px;line-height:1.1}
.brand-dot{width:10px;height:10px;border-radius:50%;background:var(--white)}
.nav{left:542px;top:38px;display:flex;gap:25px;font-size:10.5px;font-weight:600;letter-spacing:.6px;color:var(--ink);align-items:center}
.nav .phone{color:var(--red);display:flex;align-items:center;gap:5px;margin-left:-2px}
.photo{background:linear-gradient(135deg,#b8a8a6,#7c6664 60%,#a18c88)}
.hero-photo{left:535px;top:84px;width:627px;height:454px}
.hero-title{left:159px;top:190px;font-size:50px;line-height:53px}
.hero-sub{left:160px;top:315px;font-size:11px;line-height:16px;color:var(--ink)}
.btn{display:flex;align-items:center;justify-content:center;background:var(--red);color:var(--white);font-size:9.5px;font-weight:700;letter-spacing:2.3px;width:158px;height:45px;border-radius:2px}
.rule{width:43px;height:1px;background:var(--red)}
.about-photo{left:159px;top:663px;width:372px;height:379px;background:linear-gradient(135deg,#8a7567,#e4e1dc 45%,#c5c7cd)}
.eyebrow{font-size:12.5px;color:var(--text)}
.h2{font-size:50px;line-height:54px}
.para{font-size:12.8px;line-height:21.3px;color:var(--text)}
.para strong{color:var(--red);font-weight:700}
.services{left:0;top:1105px;width:1200px;height:641px;background:linear-gradient(90deg,#431022,#5a1426 50%,#4a0f22)}
.services .eyebrow,.services .para{color:#f1e3e6}
.services .h2{color:var(--white)}
.svc{background:var(--card);border-radius:2px;padding:24px 24px}
.svc h3{font-size:13.6px;font-weight:700;color:var(--ink);line-height:19px}
.svc ul{list-style:none;margin-top:13px;font-size:12.5px;line-height:20px;color:#3c3c3c}
.svc li{position:relative;padding-left:12px;margin-left:10px}
.svc li::before{content:"";position:absolute;left:0;top:9px;width:3px;height:3px;border-radius:50%;background:var(--red)}
.more{font-size:11.5px;color:var(--red);text-decoration:underline}
.svc .more{position:absolute;left:25px;bottom:24px}
.call{background:var(--red);overflow:hidden}
.call-label{font-family:"Tinos",serif;color:var(--white);font-size:16px}
.call-num{font-family:"Tinos",serif;color:var(--white);font-size:26px;font-weight:700;letter-spacing:1px}
.news-bg{left:0;top:1746px;width:1200px;height:889px;background:var(--grey)}
.center{text-align:center;left:0;width:1200px}
.post{background:#fafafa;width:282px;height:426px;box-shadow:0 2px 6px rgba(0,0,0,.05)}
.post-img{height:160px}
.post .date{position:absolute;left:26px;top:196px;font-size:9.5px;font-weight:600;color:#8a8a8a}
.post h4{position:absolute;left:26px;top:227px;width:240px;font-size:13.6px;line-height:19px;color:var(--ink);font-weight:700}
.post p{position:absolute;left:26px;top:280px;width:235px;font-size:12.3px;line-height:20px;color:#5a5a5a}
.post .more{position:absolute;left:26px;top:377px}
.footer{left:0;top:2635px;width:1200px;height:66px;background:var(--footer);color:var(--white);font-family:"Tinos",serif;font-size:11.5px}
</style>
</head>
<body>

<div class="abs hero-bg"></div>
<div class="abs brand"><span class="brand-name">Helga<br>Lindner</span><span class="brand-dot"></span></div>
<nav class="abs nav">
  <span>STARTSEITE</span><span>LEISTUNGEN</span><span>AKTUELLES</span><span>KONTAKT</span>
  <span class="phone"><svg width="16" height="16" viewBox="0 0 24 24" fill="none" stroke="currentColor" stroke-width="1.8"><path d="M5 3h4l2 5-3 2a12 12 0 006 6l2-3 5 2v4a2 2 0 01-2 2A17 17 0 013 5a2 2 0 012-2z"/></svg>0641 555018</span>
</nav>
<div class="abs photo hero-photo" role="img" aria-label="Frau am Telefon vor einem Bürofenster mit Blick auf die Stadt bei Sonnenuntergang"></div>
<h1 class="abs serif hero-title">Steuerberatung<br>in Gießen</h1>
<p class="abs hero-sub">Für Freiberufler, Gewerbetreibende, Kapitalgesellschaften,<br>Personengesellschaften und gemeinnützige Organisationen</p>
<div class="abs btn" style="left:159px;top:399px">MEHR ERFAHREN</div>

<div class="abs about-photo" role="img" aria-label="Lächelnder Berater mit Brille bespricht Unterlagen mit einem Mandanten"></div>
<p class="abs eyebrow" style="left:609px;top:666px">Wir sind für Sie da</p>
<h2 class="abs serif h2" style="left:608px;top:690px">Kompetent, schnell<br>und individuell</h2>
<div class="abs rule" style="left:609px;top:816px"></div>
<div class="abs para" style="left:609px;top:843px;width:415px">
  <p>Meine Kanzlei berät seit deren Gründung im Jahre 2003 Freiberufler, Gewerbetreibende, Kapitalgesellschaften, Personengesellschaften aus den verschiedensten Branchen sowie gemeinnützige Organisationen. Ebenso unterstützen wir gerne Existenzgründer und nebenberuflich Tätige, wie auch Arbeitnehmer, Vermieter und Rentner.</p>
  <p style="margin-top:21px">Mein Team aus erfahrenen Steuerfachangestellten und ich freuen uns, Ihnen kompetent und individuell auf Ihre persönlichen Bedürfnisse abgestimmt, bei Ihren <strong>steuerlichen Angelegenheiten</strong> zu helfen!</p>
</div>

<section class="abs services" role="img" aria-label="Historisches Fachwerkgebäude mit Bäumen, in Weinrot getönt">
</section>
<p class="abs eyebrow" style="left:159px;top:1220px;color:#f1e3e6">Das können wir für Sie tun</p>
<h2 class="abs serif h2" style="left:158px;top:1244px;color:#fff">Unsere<br>Leistungen</h2>
<div class="abs rule" style="left:159px;top:1370px"></div>
<div class="abs para" style="left:159px;top:1396px;width:290px;color:#f1e3e6">
  <p>Als zuverlässiger Partner beraten und helfen wir Ihnen rund um Fragen zu steuerlichen Themen. Wir bieten Ihnen ein Leistungsspektrum von Buchhaltung bis Lohnsteuerjahresausgleich.</p>
  <p style="margin-top:21px">Wir berücksichtigen stets aktuelle Entwicklungen.</p>
</div>
<div class="abs btn" style="left:159px;top:1564px">MEHR ERFAHREN</div>

<div class="abs svc" style="left:510px;top:1222px;width:256px;height:216px">
  <h3>Leistungen für Selbständige, Gewerbe und Existenzgründer</h3>
  <ul><li>Buchhaltung</li><li>Lohnabrechnungen</li><li>Jahresabschluss</li><li>Steuererklärungen</li></ul>
  <span class="more">Mehr erfahren »</span>
</div>
<div class="abs svc" style="left:778px;top:1222px;width:256px;height:216px">
  <h3>Leistungen<br>für Arbeitnehmer</h3>
  <ul><li>Lohnsteuerjahresausgleich</li><li>Veranlagung von Ehegatten und eingetragenen Lebenspartner schaften</li></ul>
  <span class="more">Mehr erfahren »</span>
</div>
<div class="abs svc" style="left:510px;top:1452px;width:256px;height:159px">
  <h3>Sonstige Einkünfte</h3>
  <ul><li>Rentner und Pensionäre</li><li>Vermieter</li></ul>
  <span class="more">Mehr erfahren »</span>
</div>
<div class="abs call" style="left:778px;top:1452px;width:256px;height:159px">
  <svg class="abs" style="left:6px;top:8px" width="120" height="150" viewBox="0 0 24 30" fill="none" stroke="rgba(255,255,255,.2)" stroke-width="1.4"><path d="M5 2h4l2 7-3 3a14 14 0 006 8l3-3 5 3v5a2 2 0 01-2 2A20 20 0 013 4a2 2 0 012-2z"/></svg>
  <p class="abs call-label" style="left:67px;top:40px">Wir sind für Sie da!</p>
  <p class="abs call-num" style="left:67px;top:62px">0641-55 50 18</p>
</div>

<div class="abs news-bg"></div>
<h2 class="abs serif h2 center" style="top:1800px">Aktuelles</h2>
<div class="abs rule" style="left:575px;top:1873px"></div>
<p class="abs center para" style="top:1899px">Bleiben Sie immer gut informiert. Hier erhalten Sie Einblicke in aktuelle Ereignisse.</p>

<article class="abs post" style="left:158px;top:1987px">
  <div class="photo post-img" style="background:linear-gradient(135deg,#dfe3e8,#9ea4ab)" role="img" aria-label="Weiße Autos in einem Autohaus"></div>
  <span class="date">22. JUNI 2019</span>
  <h4>Lohnsteuer: Aktuelles zum Dienstwagen</h4>
  <p>Die Privatnutzung von Dienstwagen ist für viele Arbeitnehmer ein attraktiver Lohnbestandteil, obgleich sich dieser Vorteil in aller Regel ...</p>
  <span class="more">Weiterlesen »</span>
</article>
<article class="abs post" style="left:460px;top:1987px">
  <div class="photo post-img" style="background:linear-gradient(135deg,#c9c3ba,#a8a29c 50%,#d8c8a8)" role="img" aria-label="Hand wirft einen Brief in einen Briefkasten"></div>
  <span class="date">22. JUNI 2019</span>
  <h4>Briefkastenanschrift reicht für den Vorsteuerabzug aus</h4>
  <p>Unternehmer sind zum Vorsteuerabzug berechtigt, wenn ihnen eine ordnungs­gemäße Eingangsrechnung vorliegt. Die Rechnung muss unter anderem die ...</p>
  <span class="more">Weiterlesen »</span>
</article>
<article class="abs post" style="left:761px;top:1987px">
  <div class="photo post-img" style="background:linear-gradient(135deg,#d9d6d0,#f1efeb 50%,#8b8580)" role="img" aria-label="Helles Homeoffice mit Laptop und Pflanze"></div>
  <span class="date">22. JUNI 2019</span>
  <h4>Vermietung Homeoffice vom Arbeitnehmer an den Arbeitgeber</h4>
  <p>Wenn ein Arbeitnehmer einen Raum seiner Wohnung bzw. seines Hauses an seinen Arbeitgeber vermietet und diesen Raum selbst als Homeoffice ...</p>
  <span class="more">Weiterlesen »</span>
</article>
<div class="abs btn" style="left:522px;top:2463px">ALLE NEWS LESEN</div>

<footer class="abs footer">
  <span class="abs" style="left:160px;top:26px">© 2019 Steuerberatung Lindner</span>
  <span class="abs" style="left:730px;top:26px">Impressum / Datenschutz / Haftungsausschluss</span>
  <span class="abs" style="left:1005px;top:27px;width:8px;height:8px;border-radius:50%;background:#fff"></span>
  <span class="abs" style="left:1026px;top:27px;width:8px;height:8px;background:#fff"></span>
</footer>

</body>
</html>
```